Book cover: Muddling Through Small Years (A5)

I have a book called Muddling Through Big Years. It is a book for teenagers which gives them tips and tactics on how to survive life's challenges regarding friends, family, feelings, relationships and hard stuff in life generally. I will upload the cover of this book but you can see it on my past jobs as one of the designers her eon Pixel Harbor did it for me.
I have a new book I've written called Muddling Through Small Years. This is a parallel book to Muddling Through Big Years, but it is specifically for 8 to 12 or 13 year olds, rather than for older teens.
A very important aspect of this job is that it SHOULD MATCH in some strong way - the Muddling Through Big Years book. I will be selling them together, displaying them together and I want them to look like two of a pair. It might be that you use the same image as the first book but change the colour of the image so that it is bright orange and green perhaps? Or that there is another image but in the image is placed in the exact same position across the book as the first book. It needs to look like the books are by the same author.
However, I would like this one to look a bit "younger", more kid friendly. For example, a font that looks like it is for kids, or kids' writing perhaps.
I dont want to have photos on the book, and I dont think I want cartoons or drawings - because I'm not sure how this will tie in with the first book.
I want it to look modern, fresh and designed specifically for kids. The text needs to be:
Muddling Through - Small Years!
Tips and ideas for 8 to 13 year olds about how to stay cool, calm and confident on even the toughest days!
The back cover is going to mostly just have the table of contents listed and a blurb, with one or two cartoons which I will supply. I am keen to pick a designer to just do the front cover first and will ask them to do the back cover later.
UPDATED: I have attached three files with fonts that I like.

```html
<!DOCTYPE html>
<html lang="en">
<head>
<meta charset="utf-8">
<title>Muddling Through Small Years – Front Cover</title>
<link rel="stylesheet" href="https://fonts.googleapis.com/css2?family=Gochi+Hand&family=Raleway:wght@300;400&display=swap">
<style>
  :root {
    --backdrop: #b9c9c7;
    --paper: #ffffff;
    --ink: #111111;
    --ink-soft: #222222;
    --tone-red: #e4312b;
    --tone-green: #3fd21f;
    --tone-yellow: #f3e935;
    --tone-blue: #4cc4ea;
  }
  * { margin: 0; padding: 0; box-sizing: border-box; }
  html, body {
    width: 1200px;
    height: 1000px;
    overflow: hidden;
    background: var(--backdrop);
  }
  .canvas {
    position: relative;
    width: 1200px;
    height: 1000px;
  }
  .cover {
    position: absolute;
    left: 305px;
    top: 58px;
    width: 588px;
    height: 883px;
    background: var(--paper);
  }
  .cover-title {
    position: absolute;
    top: 44px;
    left: 0;
    width: 100%;
    text-align: center;
    font-family: "Gochi Hand", cursive;
    font-weight: 400;
    font-size: 54px;
    line-height: 86px;
    letter-spacing: 0.5px;
    color: var(--ink);
    text-transform: uppercase;
    white-space: nowrap;
  }
  .cover-artwork {
    position: absolute;
    top: 225px;
    left: 0;
    width: 588px;
    height: 389px;
    display: block;
  }
  .cover-tagline {
    position: absolute;
    top: 634px;
    left: 0;
    width: 100%;
    padding: 0 56px;
    text-align: center;
    font-family: "Raleway", sans-serif;
    font-weight: 400;
    font-size: 16.5px;
    line-height: 23px;
    color: var(--ink-soft);
  }
  .author {
    position: absolute;
    top: 748px;
    left: 283px;
    width: 260px;
    text-align: center;
  }
  .author-name {
    font-family: "Gochi Hand", cursive;
    font-size: 42px;
    line-height: 48px;
    color: var(--ink);
    white-space: nowrap;
  }
  .author-role {
    font-family: "Raleway", sans-serif;
    font-weight: 400;
    font-size: 17px;
    color: var(--ink-soft);
    margin-top: 2px;
  }
</style>
</head>
<body>
  <main class="canvas">
    <section class="cover">
      <h1 class="cover-title">Muddling Through<br>Small Years!</h1>

      <svg class="cover-artwork" role="img" aria-label="Cover artwork: a crowd of glossy coloured balls in red, green, yellow and blue with one dark ball in the middle" viewBox="0 0 588 389" preserveAspectRatio="none">
        <defs>
          <linearGradient id="artwork-tones" x1="0" y1="0" x2="1" y2="1">
            <stop offset="0" stop-color="#4cc4ea"/>
            <stop offset="0.3" stop-color="#3fd21f"/>
            <stop offset="0.5" stop-color="#e4312b"/>
            <stop offset="0.75" stop-color="#f3e935"/>
            <stop offset="1" stop-color="#e4312b"/>
          </linearGradient>
        </defs>
        <rect width="588" height="389" fill="url(#artwork-tones)"/>
      </svg>

      <p class="cover-tagline">Tips and ideas for 8 to 13 year olds about how to stay cool, calm and confident on even the toughest days!</p>

      <div class="author">
        <p class="author-name">Marla Penwick</p>
        <p class="author-role">clinical psychologist</p>
      </div>
    </section>
  </main>
</body>
</html>
```